Business Card Design for Bright Canvas Hue Designs

I need a business card design for Artist Marlon Ketch who specializes in Digital Fine Art, Digital Illustration, Murals and Mixed Media. Digital art techniques combine the use of a computer and specialized programs coupled with the same methods and theories used to produce traditional art. The final design should use the new logo that was just deigned and reflect an artist who has embraced the evolution of art by using modern technology to paint vibrant, stunning and high quality art. Please make this a double sided card and use the attached photo on the back of the card. Please include the name of the business: Bright Canvas Hue Designs, Artist: Marlon Ketch, Phone: 555-283-7190 Website: brightcanvashuedesigns.example

Target Market(s)

Anyone looking for fine art for there home or business.

Industry/Entity Type

Computer

Contact Information for Business Card

This should be a double sided business card with a modern feel to it.

Font styles to use
Sans Serif

Requirements
Must have
• Artist Name: Marlon Ketch
• Business Name and Logo: Bright Canvas Hue Designs
• Phone: 555-283-7190
• Website: brightcanvashuedesigns.example
• specializes in Digital Fine Art, Digital Illustration, Murals and Mixed Media
Nice to have
• Black background with new logo that is attached to file

```html
<!DOCTYPE html>
<html lang="en">
<head>
<meta charset="utf-8">
<title>Bright Canvas Hue Designs – Business Card</title>
<link href="https://fonts.googleapis.com/css2?family=Lato:wght@400;700&display=swap" rel="stylesheet">
<style>
  :root {
    --page-bg: #e9e6e1;
    --card-white: #ffffff;
    --ink-blue: #2a37b4;
    --ink-grey: #4a4f8a;
    --accent-red: #e21d3a;
    --back-border: #c8143c;
    --back-black: #050505;
    --koi-orange: #f2a12c;
    --koi-yellow: #f6d23a;
    --wave-teal: #3fb8d4;
  }
  * { box-sizing: border-box; margin: 0; padding: 0; }
  html, body {
    width: 1200px; height: 1023px; overflow: hidden;
    background: var(--page-bg);
    font-family: "Lato", sans-serif;
  }
  .sheet {
    position: relative; width: 1200px; height: 1023px;
    display: flex; align-items: center; justify-content: center; gap: 70px;
  }
  .card-front {
    position: relative; width: 620px; height: 354px;
    background: var(--card-white);
    box-shadow: 0 6px 18px rgba(0,0,0,.18);
    color: var(--ink-blue);
  }
  .brand-mark {
    position: absolute; right: 36px; top: 38px;
    display: flex; align-items: center; gap: 12px;
  }
  .brand-mark .dot {
    width: 34px; height: 34px; border-radius: 50%;
    background: var(--accent-red);
  }
  .brand-mark .brand-name {
    font-size: 22px; font-weight: 700; color: var(--ink-blue);
    max-width: 190px; line-height: 1.1; text-align: right;
  }
  .brand-caption {
    position: absolute; right: 36px; top: 118px;
    font-size: 19px; font-weight: 400; color: var(--ink-grey);
  }
  .brand-rule {
    position: absolute; right: 36px; top: 148px; width: 300px;
    height: 2px; background: var(--accent-red);
  }
  .contact {
    position: absolute; right: 36px; top: 168px;
    list-style: none; font-size: 14px; color: var(--ink-grey);
  }
  .contact li { display: flex; align-items: center; gap: 8px; margin-bottom: 6px; }
  .contact svg { width: 13px; height: 13px; flex: none; }
  .identity {
    position: absolute; left: 36px; bottom: 34px; width: 300px;
  }
  .identity .person { font-size: 22px; font-weight: 700; }
  .identity .person .sep { color: var(--accent-red); font-weight: 400; padding: 0 4px; }
  .identity .person-rule { height: 2px; background: var(--accent-red); margin: 8px 0 10px; width: 100%; }
  .identity .studio { font-size: 21px; font-weight: 700; }
  .identity .services { font-size: 15px; line-height: 1.3; color: var(--ink-grey); margin-top: 4px; }
  .card-back {
    position: relative; width: 340px; height: 595px;
    background: var(--back-black);
    border: 14px solid var(--back-border);
    box-shadow: 0 6px 18px rgba(0,0,0,.25);
  }
  .koi-artwork {
    position: absolute; left: 22px; right: 22px; top: 40px; bottom: 70px;
    border-radius: 40% 40% 30% 30%;
    background: radial-gradient(ellipse at 45% 50%, var(--koi-yellow) 0%, var(--koi-orange) 40%, var(--wave-teal) 72%, var(--back-black) 100%);
  }
</style>
</head>
<body>
<main class="sheet">
  <section class="card-front" aria-label="Card front">
    <div class="brand-mark">
      <span class="brand-name">Bright Canvas Hue Designs</span>
      <span class="dot"></span>
    </div>
    <p class="brand-caption">Bright Canvas Hue Designs</p>
    <div class="brand-rule"></div>
    <ul class="contact">
      <li>
        <svg viewBox="0 0 16 16"><circle cx="8" cy="8" r="8" fill="var(--accent-red)"/><path d="M5 4.5c.6-.4 1.2-.2 1.5.4l.6 1.2c.2.4 0 .8-.3 1l-.5.4c.4 1 1.1 1.7 2 2.1l.4-.5c.3-.3.7-.4 1-.2l1.2.6c.6.3.7 1 .3 1.5-1 1.2-3 .6-4.6-1S3.8 5.6 5 4.5z" fill="#fff"/></svg>
        555-283-7190
      </li>
      <li>
        <svg viewBox="0 0 16 16"><circle cx="8" cy="8" r="8" fill="var(--accent-red)"/><circle cx="8" cy="8" r="4.8" fill="none" stroke="#fff" stroke-width="1"/><ellipse cx="8" cy="8" rx="2" ry="4.8" fill="none" stroke="#fff" stroke-width="1"/><line x1="3.2" y1="8" x2="12.8" y2="8" stroke="#fff" stroke-width="1"/></svg>
        www.brightcanvashuedesigns.example
      </li>
    </ul>
    <div class="identity">
      <p class="person">Marlon Ketch<span class="sep">|</span>Artist</p>
      <div class="person-rule"></div>
      <p class="studio">Bright Canvas Hue Designs</p>
      <p class="services">specializes in Digital Fine Art<br>Digital Illustration, Murals<br>and Mixed Media</p>
    </div>
  </section>
  <section class="card-back" aria-label="Card back">
    <div class="koi-artwork" role="img" aria-label="Colourful koi fish illustration swimming among turquoise waves"></div>
  </section>
</main>
</body>
</html>
```